Family farm needs a Ice Cream gift card designed for our store

Our family farm makes very popular homemade hard ice cream that we sell at our Orchard and our Garden Market store in upstate NY. In addition to selling our gift cards we want to offer an Ice Cream Gift Card that customers can purchase that entitles the bearer to a 1-scoop hard ice cream. This card would be the size of a business card (to be cost effective.) Customers could buy the card and then gift it to be used like a coupon for a free ice cream.

The front of the card will print in color but the back will be on a grayscale. The back should include basic information like physical address (for each of our locations), phone number, website and our code "PLU: 09". The card will be valid at either of our locations regardless of where it's purchased. The front of the card should be colorful and eye-catching and focus on ice cream.

We are known for our ice cream and our fresh produce, beautiful flowers and yummy prepared foods. We would like the card to evoke a farm/country/family style store.

View our website (www.brelwinfarms.com) or social media for a better idea of our style.

Industry/Entity Type

Food Store

Contact Information for Business Card

Front: Clearly shows that the gift card is valid for a 1 scoop hard ice cream. Should say business name/logo on front.
Back:
Include location addresses, PLU 09 and website.
Brelwin Orchards, 18 Maple Ridge Rd, Kinderhook, NY 12106
Brelwin's Garden Market, 42 Dover Ln, Kinderhook, NY 12106
www.brelwinfarms.com

Font styles to use
Other font styles liked:
• Our logo uses Knockout HTF52 Cruiserweight and ITC Franklin Gothic Book. Fonts similar to these are ok

Colors

Designer to choose colors to be used in the design.

Requirements
Must have
• It must clearly show that the gift card entitles the holder to a 1 scoop hard ice cream. It must be colorful and eye-catching and evoke the feeling of a farm/country store.

```html
<!DOCTYPE html>
<html lang="en">
<head>
<meta charset="utf-8">
<title>Brelwin Ice Cream Gift Card</title>
<link rel="stylesheet" href="https://fonts.googleapis.com/css2?family=Oswald:wght@400;500;600&family=Libre+Franklin:wght@400;700&display=swap">
<style>
  :root {
    --backdrop: #ece7e1;
    --red: #d03224;
    --red-light: #e04534;
    --red-text: #e0402f;
    --green: #6a8a3a;
    --white: #ffffff;
    --ray: #fbe3e0;
    --ink-gray: #555555;
    --card-gray: #dcdcdc;
    --black: #000000;
    --shadow: rgba(0,0,0,0.35);
  }
  * { margin: 0; padding: 0; box-sizing: border-box; }
  html, body { width: 1200px; height: 960px; overflow: hidden; }
  body { background: var(--backdrop); position: relative; font-family: "Oswald", sans-serif; }

  .card { position: absolute; width: 600px; height: 343px; box-shadow: 2px 3px 6px var(--shadow); overflow: hidden; }
  .card--front { left: 314px; top: 113px; background: var(--white); }
  .card--back { left: 311px; top: 472px; background: var(--card-gray); text-align: center; }

  .front-shapes { position: absolute; inset: 0; }
  .rays { position: absolute; inset: 0;
    background: radial-gradient(circle at 37% 50%, var(--white) 15%, var(--ray) 100%); }

  .store-name { position: absolute; width: 240px; left: 85px; color: var(--white); text-align: center;
    font-family: "Libre Franklin", sans-serif; }
  .store-name__main { font-size: 21px; font-weight: 700; letter-spacing: 1.5px; line-height: 1; }
  .store-name__sub { font-size: 14px; font-weight: 400; letter-spacing: 2.5px; margin-top: 5px; }
  .store-name--market { top: 18px; }
  .store-name--orchards { top: 269px; }

  .side-note { position: absolute; left: 22px; top: 142px; color: var(--white);
    font-size: 19px; font-weight: 400; line-height: 1.5; }

  .value-badge { position: absolute; left: 160px; top: 105px; width: 122px; height: 138px;
    border-radius: 52px 52px 58px 58px; background: var(--red); border: 8px solid var(--white);
    display: flex; align-items: center; justify-content: center; }
  .value-badge__amount { color: var(--white); font-size: 60px; font-weight: 600; letter-spacing: -1px; }

  .offer { position: absolute; left: 318px; top: 90px; }
  .offer__title { color: var(--red-text); font-size: 66px; font-weight: 500; line-height: 1; letter-spacing: 0.5px; }
  .offer__text { margin-top: 14px; color: var(--ink-gray); font-size: 22px; font-weight: 500; line-height: 1.35; letter-spacing: 0.3px; }

  .location__name { font-family: "Libre Franklin", sans-serif; font-weight: 700; font-size: 16.5px; letter-spacing: 0.5px; color: var(--black); line-height: 1.2; }
  .location__address { font-size: 15px; color: var(--black); margin-top: 1px; line-height: 1.3; }
  .location--orchards { margin-top: 36px; }
  .divider { width: 46px; height: 2px; background: var(--black); margin: 8px auto 9px; }
  .phone { font-size: 34px; font-weight: 400; margin-top: 4px; line-height: 1.1; color: var(--black); }
  .plu-box { display: inline-flex; align-items: center; gap: 10px; margin-top: 8px; padding: 14px 12px;
    border: 2px dotted var(--black); font-size: 15px; }
  .plu-box__value { background: var(--black); color: var(--white); padding: 1px 11px; letter-spacing: 2px; font-weight: 500; }
  .web-band { position: absolute; left: 0; right: 0; top: 295px; height: 33px; background: var(--black);
    color: var(--white); font-size: 17px; letter-spacing: 9px; line-height: 33px; }
</style>
</head>
<body>
  <section class="card card--front">
    <div class="rays" role="img" aria-label="Soft sunburst background"></div>
    <svg class="front-shapes" width="600" height="343" viewBox="0 0 600 343">
      <polygon points="0,0 402,0 222,172 355,343 0,343" fill="var(--red)"/>
      <polygon points="55,0 402,0 222,172" fill="var(--red-light)"/>
      <polygon points="0,343 222,172 355,343" fill="var(--green)"/>
    </svg>

    <div class="store-name store-name--market">
      <div class="store-name__main">BRELWIN'S</div>
      <div class="store-name__sub">GARDEN MARKET</div>
    </div>

    <p class="side-note">1 SCOOP HARD<br>ICE CREAM.</p>

    <div class="value-badge" role="img" aria-label="Apple emblem showing the card value">
      <span class="value-badge__amount">10$</span>
    </div>

    <div class="store-name store-name--orchards">
      <div class="store-name__main">BRELWIN</div>
      <div class="store-name__sub">ORCHARDS</div>
    </div>

    <div class="offer">
      <h1 class="offer__title">GIFTCARD</h1>
      <p class="offer__text">GIFT CARD IS VALID FOR<br>A 1 SCOOP<br>HARD ICE CREAM.</p>
    </div>
  </section>

  <section class="card card--back">
    <div class="location location--orchards">
      <div class="location__name">BRELWIN ORCHARDS</div>
      <div class="location__address">18 MAPLE RIDGE RD, ALDER FALLS, NY 12990</div>
    </div>
    <div class="divider"></div>
    <div class="location">
      <div class="location__name">BRELWIN'S GARDEN MARKET</div>
      <div class="location__address">42 DOVER LN, ALDER FALLS, NY 12990</div>
    </div>
    <div class="divider"></div>
    <div class="phone">(518) 555-0142</div>
    <div class="plu-box"><span>CODE</span><span class="plu-box__value">PLU: 09</span></div>
    <div class="web-band">WWW.BRELWINFARMS.COM</div>
  </section>
</body>
</html>
```